Dovel Holidays Revamp Project 2015

We are a inbound Travel and tour operator based in Kuala Lumpur, Malaysia, established since 2010. Need a vibrant, dynamic, interactive and user friendly, we expect a Content management system for self data upload.
We cater to different markets around the world form Gulf, to the Far East.
Europe to Africa. With the minimum budget we give maximum services.
The final design should communicate well with the user and portray our growth.

Here is the reference of what our current website looks like.
www.dovelholidays-example.com.my

Target Market(s)

Far-East, South East Asia, Gulf market.

Industry/Entity Type

Travel

Number of Pages Required

5+ page

Font styles to use
Serif
Sans Serif
Other font styles liked:
• Calibri

Requirements
Must have
• User interaction, User friendly, Payment integration, should have a fun interface.
Should not have
• Should not have a complicated and overcrowded or jumbled up layout.

```html
<!DOCTYPE html>
<html lang="en">
<head>
<meta charset="utf-8">
<title>Dovel Holidays</title>
<link href="https://fonts.googleapis.com/css2?family=Open+Sans:wght@300;400;600;700&display=swap" rel="stylesheet">
<style>
:root{
  --red:#c9262c;
  --red-dark:#a81d22;
  --ink:#222;
  --muted:#777;
  --line:#e3e3e3;
  --navy:#1e2a55;
  --white:#fff;
  --card-tint:#f4f6f9;
  --black:#0c0c0c;
}
*{box-sizing:border-box;margin:0;padding:0}
html,body{width:1200px;height:2889px;overflow:hidden;background:var(--white)}
body{font-family:"Open Sans",Arial,sans-serif;color:var(--ink);position:relative}
.site-header{position:absolute;top:0;left:0;width:1200px;height:89px;background:rgba(255,255,255,.93);z-index:2;display:flex;align-items:center;justify-content:space-between;padding:0 52px 0 102px}
.brand{display:flex;align-items:center;gap:12px;font-size:30px;font-weight:700;color:var(--red)}
.brand-dot{width:36px;height:36px;border-radius:50%;background:var(--red)}
.nav{display:flex;gap:0;font-size:17px;color:#333}
.nav span{padding:0 22px;border-left:2px solid #333;line-height:18px}
.nav span:first-child{border-left:0}
.nav span:last-child{padding-right:0}
.hero{position:absolute;top:0;left:0;width:1200px;height:539px;background:linear-gradient(100deg,#6f7f3a 0%,#9a9b55 35%,#c9b277 55%,#8a6e3c 75%,#4d4a25 100%)}
.hero-person{position:absolute;left:700px;top:140px;width:240px;height:399px;background:linear-gradient(#c9b79a,#8b7b62);border-radius:90px 90px 0 0;opacity:.6}
.hero-title{position:absolute;left:134px;top:270px;font-size:78px;font-weight:400;color:var(--white);line-height:1}
.hero-sub{position:absolute;left:318px;top:363px;font-size:42px;color:var(--white);line-height:1}
.hero-arrow{position:absolute;top:285px}
.promo{position:absolute;top:539px;left:0;width:1200px;height:127px;background:var(--red);border-top:5px solid var(--red-dark);border-bottom:5px solid var(--red-dark)}
.promo h2{position:absolute;left:131px;top:30px;font-size:29px;font-weight:400;color:var(--white)}
.promo p{position:absolute;left:131px;top:74px;font-size:16px;color:var(--white)}
.btn-dark{position:absolute;left:923px;top:40px;width:156px;height:44px;background:#1b1b1b;border-radius:3px;color:var(--white);font-size:19px;display:flex;align-items:center;justify-content:center}
.packages-head{position:absolute;top:708px;left:0;width:1200px;text-align:center}
.packages-head h2{font-size:34px;font-weight:300;color:#444;display:flex;align-items:center;justify-content:center;gap:26px}
.packages-head h2::before,.packages-head h2::after{content:"";width:260px;height:1px;background:#ccc}
.packages-head a{display:block;margin-top:10px;font-size:17px;color:var(--red);text-decoration:none}
.card{position:absolute;top:832px;width:299px;height:614px;border:1px solid var(--line);border-radius:5px;background:var(--white);box-shadow:0 1px 4px rgba(0,0,0,.08)}
.card h3{height:70px;display:flex;align-items:center;justify-content:center;font-size:21px;font-weight:400}
.price{background:var(--card-tint);height:120px;text-align:center;position:relative;padding-top:34px}
.price small{position:absolute;right:40px;top:12px;font-size:13px;color:var(--muted)}
.price strong{display:block;font-size:25px;font-weight:700}
.price em{display:block;font-style:normal;font-size:15px;font-weight:700;margin-top:4px}
.stays{padding:10px 18px 0}
.stays li{list-style:none;font-size:15px;border-bottom:1px solid var(--line);padding:10px 0 11px}
.card h4{font-size:24px;font-weight:400;color:var(--navy);margin:24px 18px 10px}
.incl{padding:0 28px 0 18px}
.incl li{list-style:none;font-size:14px;color:#888;border-bottom:1px solid var(--line);padding:10px 0 10px 20px;position:relative}
.incl li::before{content:"";position:absolute;left:0;top:20px;width:9px;height:1px;background:#999}
.card-foot{position:absolute;left:0;bottom:0;width:100%;height:92px;background:var(--card-tint);display:flex;align-items:center;justify-content:center}
.btn-red{width:171px;height:44px;background:var(--red);color:var(--white);font-size:18px;display:flex;align-items:center;justify-content:center}
.testimonials{position:absolute;top:1539px;left:0;width:1200px;height:370px;background:linear-gradient(#3b4446,#242c30 55%,#1a2a33)}
.testimonials h2{text-align:center;padding-top:46px;font-size:37px;font-weight:300;color:var(--white)}
.testimonials p{width:890px;margin:14px auto 0;text-align:center;font-size:15px;line-height:25px;color:#eee}
.author{position:absolute;left:480px;top:244px;display:flex;align-items:center;gap:16px}
.avatar{width:68px;height:68px;border-radius:50%;border:3px solid var(--white);background:#b47c6e}
.author b{display:block;font-size:19px;font-weight:400;color:var(--white)}
.author i{font-size:14px;color:#999}
.contact{position:absolute;top:1958px;left:0;width:1200px;text-align:center;font-size:20px;line-height:31px;color:#666}
.contact b{font-weight:400;color:var(--ink)}
.dots{width:352px;margin:6px auto 0;border-top:3px dotted #666}
.socials{display:flex;justify-content:center;gap:8px;margin-top:28px}
.socials span{width:46px;height:46px;border-radius:50%;background:#111}
.field{position:absolute;border:1px solid var(--line);border-radius:3px;font-size:14px;color:#aaa;padding:17px 27px}
.send{position:absolute;left:212px;top:2669px;width:707px;height:51px;background:var(--black);color:var(--white);font-size:20px;display:flex;align-items:center;justify-content:center}
.site-footer{position:absolute;top:2773px;left:0;width:1200px;height:116px;background:var(--red)}
.site-footer .brand{position:absolute;left:100px;top:38px;color:var(--white)}
.site-footer .brand-dot{background:var(--white)}
.site-footer .nav{position:absolute;right:50px;top:36px;color:var(--white)}
.site-footer .nav span{border-color:var(--white)}
.copy{position:absolute;right:50px;top:77px;font-size:13px;color:var(--white)}
</style>
</head>
<body>
<header class="site-header">
  <div class="brand"><span class="brand-dot"></span>Dovel Holidays</div>
  <nav class="nav"><span>Agents</span><span>My Booking</span><span>Destinations</span><span>Travel offers</span></nav>
</header>

<section class="hero" role="img" aria-label="Sunlit forest with a smiling backpacker giving a thumbs up">
  <div class="hero-person"></div>
  <h1 class="hero-title">Travel With Us</h1>
  <div class="hero-sub">For The Best Deal</div>
  <svg class="hero-arrow" style="left:68px" width="26" height="60" viewBox="0 0 26 60"><polyline points="24,2 2,30 24,58" fill="none" stroke="#fff" stroke-width="2" opacity=".8"/></svg>
  <svg class="hero-arrow" style="left:1108px" width="26" height="60" viewBox="0 0 26 60"><polyline points="2,2 24,30 2,58" fill="none" stroke="#fff" stroke-width="2" opacity=".8"/></svg>
</section>

<section class="promo">
  <h2>Complete Travel Package For Your Holidays</h2>
  <p>Duis molliest non commodo luctus nisi erat porttitor ligula deleget lacin Lorem ipsum dolor sit amet.</p>
  <div class="btn-dark">read more</div>
</section>

<div class="packages-head">
  <h2>Most Popular Packages</h2>
  <a href="#">view all packages</a>
</div>

<article class="card" style="left:133px">
  <h3>Option#1 (3 Star)</h3>
  <div class="price"><small>per person</small><strong>COST: US $299</strong><em>(3 Star Metra Hotel/ Sera Vista)</em></div>
  <ul class="stays"><li>3 Nights Metra Hotel, Kuala lumpur</li><li style="border:0">2 Night Sera Vista Hotel, Langkawi</li></ul>
  <h4>Package Inclusion :-</h4>
  <ul class="incl"><li>Accommodation with bfast</li><li>Kuala Lumpur Half day City tour</li><li>Sunray Lagoon tour + Ticket</li><li>Langkawi Island Tour</li><li>Lgk transfer Jetty/Htl/Apt</li></ul>
  <div class="card-foot"><div class="btn-red">Know more...</div></div>
</article>

<article class="card" style="left:458px">
  <h3>Option#2 ( 4 Star )</h3>
  <div class="price"><small>per person</small><strong>COST: US $299</strong><em>(3 Star Metra Hotel/ Sera Vista)</em></div>
  <ul class="stays"><li>3 Nights Alpen Hotel, Kuala lumpur</li><li style="border:0">2 Nights Palma Villa Hotel, Langkawi</li></ul>
  <h4>Package Inclusion :-</h4>
  <ul class="incl"><li>Accommodation with bfast</li><li>Kuala Lumpur Half day City tour</li><li>Sunray Lagoon tour + Ticket</li><li>Langkawi Island Tour</li><li>Lgk transfer Jetty/Htl/Apt</li></ul>
  <div class="card-foot"><div class="btn-red">Know more...</div></div>
</article>

<article class="card" style="left:782px">
  <h3>Option#3 ( 5 Star )</h3>
  <div class="price"><small>per person</small><strong>COST: US $299</strong><em>(3 Star Metra Hotel/ Sera Vista)</em></div>
  <ul class="stays"><li>3 Nights Grand Square, Kuala lumpur</li><li>2 Nights Heron Hotel, Penang</li><li style="border:0">2 Night Sera Vista Hotel, Langkawi</li></ul>
  <h4>Package Inclusion :-</h4>
  <ul class="incl"><li>Accommodation with bfast</li><li>Kuala Lumpur Half day City tour</li><li>Sunray Lagoon tour + Ticket</li><li>Langkawi Island Tour</li></ul>
  <div class="card-foot"><div class="btn-red">Know more...</div></div>
</article>

<section class="testimonials" role="img" aria-label="Resort pool with loungers and thatched villas at dusk">
  <h2>Tourists Testimonials</h2>
  <p>Lorem ipsum dolor sit amet, consectetur adipisicing elit, sed do eiusmod tempor incididunt ut labore et dolore magna aliqua. Ut enim ad minim veniam, quis nostrud exercitation ullamco laboris nisi ut aliquip ex ea commodo consequat.Etiam porta sem malesuada magna mollis euismod. Nullam quis risus eget urna mollis ornare vel eu leo. Fusce dapibus, Aenean e u leo quam. Pellentesque ornare sem lacinia.</p>
  <div class="author"><div class="avatar" role="img" aria-label="Portrait of the reviewer"></div><div><b>Mira Tan</b><i>Editor of Wander Journal</i></div></div>
</section>

<section class="contact">
  <svg width="30" height="42" viewBox="0 0 30 42" style="display:block;margin:0 auto 6px"><path d="M15 0C6.7 0 0 6.7 0 15c0 11 15 27 15 27s15-16 15-27C30 6.7 23.3 0 15 0z" fill="#c9262c"/><circle cx="15" cy="15" r="5.5" fill="#fff"/></svg>
  <div><b>Head Office:</b> Suite No. 8</div>
  <div>No.42 Jalan Seri Kenanga Kuala Lumpur . Malaysia.</div>
  <div>Suite No. 210, 2nd Floor Menara Cempaka</div>
  <div>T: +603 2000 5500</div>
  <div><b>E:</b> tours@dovelholidays-example.com.my</div>
  <div><b>W:</b> www.dovelholidays-example.com.my</div>
  <div class="dots"></div>
  <div class="socials"><span></span><span></span><span></span><span></span></div>
</section>

<form>
  <div class="field" style="left:212px;top:2352px;width:341px;height:54px">name</div>
  <div class="field" style="left:580px;top:2352px;width:343px;height:54px">e-mail</div>
  <div class="field" style="left:212px;top:2431px;width:341px;height:56px">phone</div>
  <div class="field" style="left:580px;top:2431px;width:343px;height:56px">address</div>
  <div class="field" style="left:212px;top:2510px;width:707px;height:135px">message</div>
  <div class="send">Send</div>
</form>

<footer class="site-footer">
  <div class="brand"><span class="brand-dot"></span>Dovel Holidays</div>
  <nav class="nav"><span>Agents</span><span>My Booking</span><span>Destinations</span><span>Travel offers</span></nav>
  <div class="copy">Copyright © 2014 All Right Reserved, Dovel holidays.</div>
</footer>
</body>
</html>
```